Quick Order Banner Design

We want to build a banner that will sit in the middle of the page that will replace our current quick order banner that we don't like. See https://www.snapglimmer.com/image/48273916?key=3f9b2c81d4e6a07f5c1b9e2d7a84f630

Text:
Quick Order is a fast and easy way to fill your cart with items when you know exactly what you want to purchase.

Design ideas:

Use foto Noto Sans. Color codes can be of #00539E, FDBC38, #6AC07A

We don't want a computer screen in banner nor a person. You can look at our competitors below for ideas.

i don't like the design here https://toblinmobilebits.com/blog/post/order-parts-fast-with-our-new-quick-order-feature but the concept is cool as it shows where to access it.. but i want other ideas too.

Our staging server is pelvant7.com

Our competitors:
https://www.quillonsupply.com/
https://www.brevolt.com/
https://www.zoska.com/
https://www.vimbo.com/index.html

Target Market(s)

B2B, Contractors who buy our products

Industry/Entity Type

hvac

Requirements
Should not have
• people photos or computer or computer screens.

```html
<!DOCTYPE html>
<html lang="en">
<head>
<meta charset="utf-8">
<title>Quick Order Banner</title>
<link rel="stylesheet" href="https://fonts.googleapis.com/css2?family=Noto+Sans:wght@400;600;700;800&display=swap">
<style>
  :root {
    --page-bg: #e3e4e6;
    --brand-blue: #0a4a98;
    --brand-blue-band: #0057a8;
    --brand-blue-deep: #003f87;
    --brand-yellow: #fdbc38;
    --white: #ffffff;
    --ink: #3a3d42;
    --ink-soft: #6b6f75;
    --line: #d9dbde;
    --step-btn: #4a4e54;
    --panel-top: #6c7075;
    --panel-bottom: #4b4f55;
    --accent-orange: #f07c1c;
    --action-blue: #0b4d9c;
  }
  * { box-sizing: border-box; margin: 0; padding: 0; }
  html, body { width: 1200px; height: 636px; overflow: hidden; }
  body { background: var(--page-bg); font-family: "Noto Sans", sans-serif; position: relative; }

  .banner {
    position: absolute; left: 30px; top: 150px; width: 1142px; height: 326px;
    background: var(--white); overflow: hidden;
    box-shadow: 0 10px 14px rgba(0,0,0,0.28);
  }
  .banner__shapes { position: absolute; inset: 0; }

  .pitch { position: absolute; left: 37px; top: 30px; color: var(--white); }
  .pitch__title { color: var(--brand-yellow); font-weight: 700; font-size: 62px; line-height: 1; letter-spacing: 1px; }
  .pitch__lead { margin-top: 8px; font-weight: 700; font-size: 36px; line-height: 44px; }
  .pitch__cta {
    display: block; margin-top: 20px; margin-left: 3px; width: 203px; height: 40px;
    background: var(--white); color: var(--brand-blue-deep);
    font-weight: 700; font-size: 26px; line-height: 40px; text-align: center; text-decoration: none;
  }

  .order { position: absolute; left: 647px; top: 0; width: 495px; height: 326px; color: var(--ink); }
  .order__title { position: absolute; left: 0; top: 6px; font-size: 14.5px; font-weight: 700; color: #4a4d52; }
  .order__intro { position: absolute; left: 0; top: 33px; font-size: 5.4px; color: var(--ink-soft); white-space: nowrap; }

  .order__table { position: absolute; left: 0; top: 63px; width: 350px; height: 240px; border: 1px solid var(--line); border-right: none; }
  .order__head { position: absolute; left: 0; top: 0; width: 100%; height: 24px; border-bottom: 1px solid var(--line); font-size: 6.4px; font-weight: 700; }
  .order__head span { position: absolute; top: 8px; }
  .row { position: absolute; left: 0; width: 100%; height: 27px; }
  .row__field { position: absolute; left: 7px; top: 5px; width: 171px; height: 17px; border: 1px solid #b9bcc0; font-size: 5.4px; color: var(--ink-soft); padding-left: 6px; line-height: 15px; }
  .row__photo { position: absolute; top: 2px; width: 20px; height: 23px; }
  .row__qty { position: absolute; left: 226px; top: 5px; display: flex; }
  .row__qty .step { width: 15px; height: 17px; background: var(--step-btn); color: var(--white); font-size: 8px; line-height: 17px; text-align: center; }
  .row__qty .count { width: 22px; height: 17px; border: 1px solid #c6c8cb; font-size: 5.5px; text-align: center; line-height: 15px; }
  .row__price { position: absolute; left: 296px; top: 11px; font-size: 5.4px; }
  .row__remove { position: absolute; left: 335px; top: 9px; width: 5px; height: 7px; background: var(--step-btn); border-radius: 1px; }
  .order__more { position: absolute; left: 7px; top: 183px; font-size: 5.2px; color: var(--action-blue); }
  .order__subtotal { position: absolute; left: 263px; top: 197px; font-size: 6px; font-weight: 700; }
  .btn { background: var(--action-blue); color: var(--white); font-size: 6px; font-weight: 700; text-align: center; }
  .order__add { position: absolute; left: 263px; top: 213px; width: 59px; height: 16px; line-height: 16px; }

  .import { position: absolute; left: 350px; top: 63px; width: 111px; height: 240px; color: var(--white); }
  .import__top { position: absolute; inset: 0 0 120px 0; background: var(--panel-top); }
  .import__bottom { position: absolute; left: 0; right: 0; top: 120px; bottom: 0; background: var(--panel-bottom); }
  .import h3 { position: absolute; left: 20px; font-size: 6.2px; font-weight: 700; }
  .import__icon { position: absolute; left: 7px; width: 7px; height: 8px; border: 1.2px solid var(--white); }
  .import__drop { position: absolute; left: 8px; top: 21px; width: 96px; height: 72px; border: 1px dashed #c9cbce; text-align: center; font-size: 4.8px; line-height: 7px; padding-top: 9px; }
  .import__choose { margin: 7px auto 0; width: 59px; height: 11px; line-height: 11px; font-size: 5px; }
  .import__sample { display: block; margin-top: 7px; font-size: 5px; text-decoration: underline; }
  .import__tutorial { position: absolute; left: 26px; top: 101px; width: 59px; height: 12px; background: var(--accent-orange); font-size: 5px; font-weight: 700; text-align: center; line-height: 12px; }
  .import__note { position: absolute; left: 8px; top: 143px; width: 96px; font-size: 4.8px; line-height: 7px; }
  .import__example { position: absolute; left: 8px; top: 171px; width: 96px; height: 46px; background: var(--white); color: var(--ink); font-size: 4.8px; line-height: 7px; padding: 4px 5px; }
  .import__paste-add { position: absolute; left: 8px; top: 221px; width: 96px; height: 12px; line-height: 12px; font-size: 5px; }
</style>
</head>
<body>
  <section class="banner">
    <svg class="banner__shapes" width="1142" height="326" viewBox="0 0 1142 326" aria-hidden="true">
      <polygon points="480,0 530,0 626,196 590,196" fill="var(--brand-yellow)"/>
      <polygon points="0,0 455,0 638,326 0,326" fill="var(--brand-blue)"/>
      <polygon points="455,0 492,0 677,326 638,326" fill="var(--brand-blue-band)"/>
    </svg>

    <div class="pitch">
      <h1 class="pitch__title">QUICK ORDER</h1>
      <p class="pitch__lead">A simple and quick way<br>to streamline ordering the<br>products you need.</p>
      <a class="pitch__cta" href="#">Try Now</a>
    </div>

    <div class="order">
      <h2 class="order__title">Quick Order</h2>
      <p class="order__intro">Quick Order is the fastest and easiest way to place your orders online. You can use the single item search below to enter product name / SKU or use the bulk csv import option.</p>

      <div class="order__table">
        <div class="order__head">
          <span style="left:7px">Product Name / SKU</span>
          <span style="left:192px">Photo</span>
          <span style="left:249px">Qty</span>
          <span style="left:296px">Price</span>
        </div>

        <div class="row" style="top:26px">
          <div class="row__field">Valora, KR418T307</div>
          <div class="row__photo" role="img" aria-label="Outdoor condenser unit product thumbnail" style="left:192px;background:linear-gradient(#8a6a4e,#5e4634)"></div>
          <div class="row__qty"><span class="step">−</span><span class="count">1</span><span class="step">+</span></div>
          <span class="row__price">$3,410.00</span><span class="row__remove"></span>
        </div>
        <div class="row" style="top:60px">
          <div class="row__field">Valora, HLM240Q16</div>
          <div class="row__photo" role="img" aria-label="Indoor air handler product thumbnail" style="left:196px;width:12px;top:-2px;height:27px;background:linear-gradient(#a08466,#6f5440)"></div>
          <div class="row__qty"><span class="step">−</span><span class="count">1</span><span class="step">+</span></div>
          <span class="row__price">$1,070.00</span><span class="row__remove"></span>
        </div>
        <div class="row" style="top:91px">
          <div class="row__field">Enter Product Name or SKU to Add</div>
          <div class="row__qty"><span class="step">−</span><span class="count"></span><span class="step">+</span></div>
          <span class="row__price">$0.00</span><span class="row__remove"></span>
        </div>
        <div class="row" style="top:118px">
          <div class="row__field">Enter Product Name or SKU to Add</div>
          <div class="row__qty"><span class="step">−</span><span class="count"></span><span class="step">+</span></div>
          <span class="row__price">$0.00</span><span class="row__remove"></span>
        </div>
        <div class="row" style="top:145px">
          <div class="row__field">Enter Product Name or SKU to Add</div>
          <div class="row__qty"><span class="step">−</span><span class="count"></span><span class="step">+</span></div>
          <span class="row__price">$0.00</span><span class="row__remove"></span>
        </div>

        <span class="order__more">+ Add Additional Rows</span>
        <span class="order__subtotal">Subtotal: $4,480.00</span>
        <div class="btn order__add">Add To Cart</div>
      </div>

      <aside class="import">
        <div class="import__top">
          <span class="import__icon" style="top:8px"></span>
          <h3 style="top:8px">Import Your Order</h3>
          <div class="import__drop">
            Drag and drop a .CSV file here,<br>or select file from your computer<br>to import to cart.
            <div class="btn import__choose">Choose File</div>
            <span class="import__sample">Download Sample CSV</span>
          </div>
          <div class="import__tutorial">◷ Tutorial</div>
        </div>
        <div class="import__bottom"></div>
        <span class="import__icon" style="top:127px"></span>
        <h3 style="top:127px">Paste Your Order</h3>
        <p class="import__note">Copy and paste or manually enter your order with the SKU # and quantity, separated by a comma on each line.</p>
        <div class="import__example">Example:<br><br>PTN36D410,1<br>M4-83015926472,2</div>
        <div class="btn import__paste-add">Add to Cart</div>
      </aside>
    </div>
  </section>
</body>
</html>
```